New Template, new corporate image Datavista 2022

New template designs for google slides or PowerPoint. Match to new corporate image. The new website www.datavista-mx.example Needs to match our new version. Technology and Artificial Intelligence elements to reflect our type of work.
We are adding old version of template and will send elements for the new corporate images.
Please consider our website as the main corporate image.
Our templates are being used on customer presentations, webminars, internal work only.
We have our main name of company Datavista. Datavista has to be in all the templates.
Secondary logo or branded service is: Quorvitar.

Target Market(s)

Industrial users. Asset managers. Corporate visitors and customers.

Industry/Entity Type

Automotive. Chemical. Food and Beverage. Manufacturing

Font styles to use
Other font styles liked:
• GE INSPIRA. RALEWAY

Colors
0054AA
0677BA
7BADD7
CADEEF
E8F1F8

Requirements
Must have
• Match to our elements on the new image. Use Brain Icons. Chips icons to connect equipments with software and control. Innovation.
Nice to have
• Unique images, machine images. Connecting machines and data elements. Template version for google slides. Image for industrial software for control equipment and saving money to manufacturers. Segments: Automotive, Chemical, Food and Beverages, Mining and pharmaceutical, Energy Management
Should not have
• old elements. not to much images of medical devices. Do not seems like a hospital.

```html
<!DOCTYPE html>
<html lang="en">
<head>
<meta charset="utf-8">
<title>Datavista 2022 – Presentation Template</title>
<link href="https://fonts.googleapis.com/css2?family=Raleway:wght@300;400;500;600;700&display=swap" rel="stylesheet">
<style>
:root{
  --navy:#0054AA;
  --blue:#0677BA;
  --sky:#7BADD7;
  --mist:#CADEEF;
  --ice:#E8F1F8;
  --bright:#2a92dc;
  --ink:#222831;
  --grey:#8c8f94;
  --dark:#050d1c;
  --board:#9e9e9e;
  --white:#ffffff;
}
*{box-sizing:border-box;margin:0;padding:0}
html,body{width:1200px;height:3165px;overflow:hidden}
body{position:relative;background:var(--board);font-family:'Raleway',sans-serif;color:var(--ink)}

.hero{position:absolute;left:0;top:0;width:1200px;height:800px;background:linear-gradient(180deg,#e4e8ee 0%,#cfd4db 60%,#a9abae 100%)}
.hero-brand{position:absolute;left:845px;top:92px;font-size:46px;font-weight:500;color:var(--blue);letter-spacing:.5px}
.hero-slide{position:absolute;left:150px;top:175px;transform:scale(1.35);transform-origin:0 0;box-shadow:0 18px 40px rgba(0,0,0,.35)}

.slide{position:absolute;width:562px;height:316px;overflow:hidden;background:var(--white)}
.col-l{left:28px}.col-r{left:609px}.col-c{left:319px}
.abs{position:absolute}
.center{left:0;right:0;text-align:center}

.brand{font-weight:500;color:var(--bright);font-size:22px;letter-spacing:.3px}
.brand.white{color:var(--white)}
.brand.blue{color:var(--blue)}

.photo-dark{position:absolute;inset:0;background:radial-gradient(ellipse at 70% 45%,#0c3f78 0%,#06203f 35%,#030a17 75%)}
.photo-tunnel{position:absolute;inset:0;background:radial-gradient(ellipse at 50% 50%,#0d4a7c 0%,#0a2a4f 40%,#04101f 80%)}
.brain{position:absolute;left:315px;top:0;width:222px;height:296px;background:radial-gradient(ellipse at 55% 38%,rgba(80,190,255,.75) 0%,rgba(20,110,200,.45) 28%,rgba(6,40,80,0) 62%)}
.hex-light{position:absolute;inset:0;background:linear-gradient(160deg,#f7f9fb 0%,#eceff3 100%)}

.t-title{font-weight:700;color:var(--bright);font-size:27px;line-height:31px}
.t-sub{font-weight:300;color:var(--white);font-size:15px}
.pill{position:absolute;height:17px;background:var(--blue);color:var(--white);font-size:7.5px;font-weight:600;display:flex;align-items:center;justify-content:center;border-radius:2px}
.strip{position:absolute;left:0;right:0;bottom:0;height:19px;display:flex;align-items:center;justify-content:center;font-size:6.5px;letter-spacing:1px;color:var(--sky)}
.strip.light{background:var(--white)}
.strip.dark{background:#2a2f36}

.s-title{position:absolute;left:0;right:0;top:20px;text-align:center;font-weight:700;font-size:20px;color:var(--ink)}
.foot-brand{position:absolute;left:17px;top:282px;font-size:15px;font-weight:500;color:var(--blue)}
.foot-bar{position:absolute;left:119px;top:285px;width:400px;height:10px;background:var(--blue)}
.foot-num{position:absolute;left:527px;top:285px;width:35px;height:10px;background:var(--sky);color:var(--white);font-size:5px;display:flex;align-items:center;justify-content:center}

.dot{position:absolute;border-radius:50%;display:flex;align-items:center;justify-content:center}
.ring{border:2px solid var(--blue);background:var(--white)}
.fill-navy{background:var(--blue)}
.fill-sky{background:var(--sky)}
.fill-grey{background:#9a9ca0}
.hd{font-size:12.5px;font-weight:400;color:var(--bright);line-height:14px}
.hd.sky{color:var(--sky)}
.hd.grey{color:var(--grey)}
.tiny{font-size:6.8px;line-height:8px;color:#333}
.mini{font-size:6px;line-height:7px;color:#444}

.agenda-num{position:absolute;width:20px;height:20px;border-radius:50%;color:var(--white);font-size:9px;font-weight:700;display:flex;align-items:center;justify-content:center}
.ag-t{position:absolute;font-size:13px;color:var(--bright)}
.ag-t.sky{color:var(--sky)}
.ag-t.grey{color:#8a8d92}
.ag-t.dark{color:var(--ink)}
.ag-s{display:block;font-size:7px;color:#333;margin-top:2px}

.svc{position:absolute;width:170px}
.svc.r{text-align:right}
.svc .hd{font-size:11.5px}

.ind-band{position:absolute;left:0;top:0;width:562px;height:157px;background:linear-gradient(160deg,#0a64b8 0%,var(--navy) 60%,#08488e 100%)}
.ind{position:absolute;width:100px;text-align:center}
.ind .hd{font-size:11px}

.case-photo{position:absolute;width:78px;height:78px;border-radius:50%;background:radial-gradient(circle at 40% 40%,#9aa7b6 0%,#4c5a6b 60%,#2a3442 100%)}
.case{position:absolute;width:170px}
.case .hd{font-size:10.5px;line-height:11px}
.case .mini{font-size:5.2px;line-height:6px;margin-top:2px}
.case .hl{font-size:6px;color:var(--sky);margin-top:3px;line-height:7px}

.contact{position:absolute;left:54px;top:96px;color:var(--white)}
.contact h3{font-weight:400;font-size:13.5px;margin-top:18px}
.contact .addr{font-size:7px;line-height:8px;margin-top:6px}
.contact ul{list-style:none;margin-top:14px}
.contact li{display:flex;align-items:center;gap:8px;font-size:7px;height:16px}
</style>
</head>
<body>

<section class="hero">
  <div class="hero-brand">Datavista</div>
  <div class="slide hero-slide">
    <div class="photo-dark" role="img" aria-label="Dark blue technology background with circuit lines"></div>
    <div class="brain" role="img" aria-label="Glowing blue brain over a circuit chip"></div>
    <div class="abs brand" style="left:44px;top:46px">Datavista</div>
    <div class="abs t-title" style="left:44px;top:116px">Presentation<br>Title Goes Here</div>
    <div class="abs t-sub" style="left:44px;top:184px">Subtitle of Presentation Goes Here!</div>
    <div class="pill" style="left:44px;top:232px;width:133px">Saturday, January 15, 2022</div>
    <div class="strip light">Copyright © Datavista</div>
  </div>
</section>

<!-- Row 1 -->
<div class="slide col-l" style="top:809px">
  <div class="photo-dark" role="img" aria-label="Dark blue technology background with circuit lines"></div>
  <div class="brain" role="img" aria-label="Glowing blue brain over a circuit chip"></div>
  <div class="abs brand" style="left:44px;top:46px">Datavista</div>
  <div class="abs t-title" style="left:44px;top:116px">Presentation<br>Title Goes Here</div>
  <div class="abs t-sub" style="left:44px;top:184px">Subtitle of Presentation Goes Here!</div>
  <div class="pill" style="left:44px;top:232px;width:133px">Saturday, January 15, 2022</div>
  <div class="strip light">Copyright © Datavista</div>
</div>
<div class="slide col-r" style="top:809px">
  <div class="photo-dark" role="img" aria-label="Dark blue technology background with circuit lines"></div>
  <div class="brain" role="img" aria-label="Glowing blue brain over a circuit chip"></div>
  <div class="abs brand" style="left:44px;top:46px">Datavista</div>
  <div class="abs t-title" style="left:44px;top:116px">Presentation<br>Title Goes Here</div>
  <div class="abs t-sub" style="left:44px;top:184px">Subtitle of Presentation Goes Here!</div>
  <div class="pill" style="left:44px;top:232px;width:133px">Saturday, January 15, 2022</div>
  <div class="strip dark">Copyright © Datavista</div>
</div>

<!-- Row 2 -->
<div class="slide col-l" style="top:1145px">
  <div class="photo-tunnel" role="img" aria-label="Blue data tunnel with glowing circuit lights"></div>
  <div class="abs center brand" style="top:54px">Datavista</div>
  <div class="abs center t-title" style="top:116px">Presentation Title<br>Goes Here</div>
  <div class="abs center t-sub" style="top:184px">Subtitle of Presentation Goes Here!</div>
  <div class="pill" style="left:215px;top:232px;width:131px">Saturday, January 15, 2022</div>
  <div class="strip light">Copyright © Datavista</div>
</div>
<div class="slide col-r" style="top:1145px">
  <div class="hex-light"></div>
  <div class="abs center brand blue" style="top:54px">Datavista</div>
  <div class="abs center t-title" style="top:116px;color:var(--blue)">Presentation Title<br>Goes Here</div>
  <div class="abs center t-sub" style="top:184px;color:#8a8d92">Subtitle of Presentation Goes Here!</div>
  <div class="pill" style="left:215px;top:232px;width:131px">Saturday, January 15, 2022</div>
  <div class="strip dark">Copyright © Datavista</div>
</div>

<!-- Row 3 -->
<div class="slide col-l" style="top:1479px">
  <div class="s-title">Agenda Slide</div>
  <div class="abs" style="left:76px;top:154px;font-weight:700;font-size:19px">Tópicos Hoy</div>
  <svg class="abs" style="left:0;top:0" width="562" height="316">
    <path d="M225 71 Q350 165 225 259" fill="none" stroke="#c9c9c9" stroke-width="6"/>
  </svg>
  <div class="agenda-num fill-navy" style="left:254px;top:72px">1</div>
  <div class="agenda-num fill-sky" style="left:303px;top:128px">2</div>
  <div class="agenda-num fill-grey" style="left:303px;top:183px">3</div>
  <div class="agenda-num" style="left:254px;top:238px;background:#1d1f23">4</div>
  <div class="ag-t" style="left:306px;top:70px">Your Title Goes Here<span class="ag-s">Your Subtitle Goes Here</span></div>
  <div class="ag-t sky" style="left:336px;top:126px">Your Title Goes Here<span class="ag-s">Your Subtitle Goes Here</span></div>
  <div class="ag-t grey" style="left:336px;top:181px">Your Title Goes Here<span class="ag-s">Your Subtitle Goes Here</span></div>
  <div class="ag-t dark" style="left:306px;top:234px">Your Title Goes Here<span class="ag-s">Your Subtitle Goes Here</span></div>
  <div class="foot-brand">Datavista</div><div class="foot-bar"></div><div class="foot-num">5</div>
</div>
<div class="slide col-r" style="top:1479px">
  <div class="hex-light"></div>
  <div class="s-title">About us</div>
  <p class="abs tiny" style="left:40px;width:482px;top:64px;text-align:center;font-size:8.6px;line-height:9.5px">We are specialists in automation, process control, information technologies, development and consulting for quality, efficiency and production. Our goal is to always provide the best solutions in conjunction with our technology partners Corvalink.</p>
  <div class="dot ring" style="left:86px;top:116px;width:52px;height:52px"><svg width="22" height="22" viewBox="0 0 22 22" fill="none" stroke="#0677BA" stroke-width="1.6"><rect x="5" y="5" width="12" height="12"/><path d="M8 2v3M11 2v3M14 2v3M8 17v3M11 17v3M14 17v3M2 8h3M2 14h3M17 8h3M17 14h3"/></svg></div>
  <div class="dot ring" style="left:255px;top:116px;width:52px;height:52px"><svg width="22" height="22" viewBox="0 0 22 22" fill="none" stroke="#0677BA" stroke-width="1.6"><path d="M11 2l8 4.5v9L11 20l-8-4.5v-9z M3 6.5l8 4.5 8-4.5 M11 11v9"/></svg></div>
  <div class="dot ring" style="left:424px;top:116px;width:52px;height:52px"><svg width="22" height="22" viewBox="0 0 22 22" fill="none" stroke="#0677BA" stroke-width="1.6"><circle cx="11" cy="11" r="8"/><path d="M3 11h16M11 3c4 4 4 12 0 16M11 3c-4 4-4 12 0 16"/></svg></div>
  <div class="abs hd" style="left:37px;width:150px;top:178px;text-align:center">Smart<br>Machines</div>
  <div class="abs hd" style="left:206px;width:150px;top:178px;text-align:center">Operational<br>Excellence</div>
  <div class="abs hd" style="left:375px;width:150px;top:178px;text-align:center">Industrial<br>Internet</div>
  <p class="abs tiny" style="left:40px;width:145px;top:212px;text-align:center">Intelligent machines in operation and control, in the same synchronization regardless of the brand installed. Efficiency that saves in operation. Creating brilliant machines.</p>
  <p class="abs tiny" style="left:209px;width:145px;top:212px;text-align:center">Operational excellence is part of our language, strengthening the ties of efficiency in the company delivers revolutionary results. Saving and producing is easy with the experts.</p>
  <p class="abs tiny" style="left:378px;width:145px;top:212px;text-align:center">Extending the Internet to industrial operation will exceed global energy savings by more than 1 Billion USD. A new generation of systems emerges, be part of this revolution.</p>
  <div class="foot-brand">Datavista</div><div class="foot-bar"></div><div class="foot-num">6</div>
</div>

<!-- Row 4 -->
<div class="slide col-l" style="top:1814px">
  <div class="s-title">Services</div>
  <div class="svc r" style="left:45px;top:84px"><div class="hd">Tech Support</div><p class="mini">We provide solutions to any event, we have a team of experts in industrial automation.</p></div>
  <div class="svc r" style="left:45px;top:142px"><div class="hd">Tech Courses</div><p class="mini">We offer completely customized courses based on the need of our customers.</p></div>
  <div class="svc r" style="left:45px;top:200px"><div class="hd">Consultory</div><p class="mini">We offer the most advanced in industrial technology, Hardware and Software update.</p></div>
  <div class="dot ring" style="left:232px;top:87px;width:42px;height:42px"><svg width="18" height="18" viewBox="0 0 18 18" fill="none" stroke="#0677BA" stroke-width="1.5"><path d="M3 11V9a6 6 0 0 1 12 0v2"/><rect x="2" y="10" width="3" height="5"/><rect x="13" y="10" width="3" height="5"/></svg></div>
  <div class="dot ring" style="left:286px;top:87px;width:42px;height:42px"><svg width="18" height="18" viewBox="0 0 18 18" fill="none" stroke="#0677BA" stroke-width="1.5"><path d="M1 7l8-4 8 4-8 4z M5 9v4c2 2 6 2 8 0V9"/></svg></div>
  <div class="dot ring" style="left:232px;top:144px;width:42px;height:42px"><svg width="18" height="18" viewBox="0 0 18 18" fill="none" stroke="#0677BA" stroke-width="1.5"><rect x="2" y="3" width="14" height="9"/><path d="M6 15h6M9 12v3"/></svg></div>
  <div class="dot ring" style="left:286px;top:144px;width:42px;height:42px"><svg width="18" height="18" viewBox="0 0 18 18" fill="none" stroke="#0677BA" stroke-width="1.5"><path d="M4 2h7l3 3v11H4z M7 9h5M7 12h5"/></svg></div>
  <div class="dot ring" style="left:232px;top:201px;width:42px;height:42px"><svg width="18" height="18" viewBox="0 0 18 18" fill="none" stroke="#0677BA" stroke-width="1.5"><circle cx="9" cy="9" r="7"/><path d="M2 9h14M9 2c3 3 3 11 0 14M9 2c-3 3-3 11 0 14"/></svg></div>
  <div class="dot ring" style="left:286px;top:201px;width:42px;height:42px"><svg width="18" height="18" viewBox="0 0 18 18" fill="none" stroke="#0677BA" stroke-width="1.5"><path d="M2 8l4-3 3 2 3-2 4 3-5 5-2-1-2 1z"/></svg></div>
  <div class="svc" style="left:347px;top:82px"><div class="hd">Certification</div><p class="mini">We offer official certifications based on the need of our customers.</p></div>
  <div class="svc" style="left:347px;top:140px"><div class="hd">Diagnostics</div><p class="mini">We offer the most advanced in industrial technology, Hardware and Software update.</p></div>
  <div class="svc" style="left:347px;top:198px"><div class="hd">Customer Attention</div><p class="mini">We offer the most advanced in industrial technology, Hardware and Software update.</p></div>
  <div class="foot-brand">Datavista</div><div class="foot-bar"></div><div class="foot-num">7</div>
</div>
<div class="slide col-r" style="top:1814px">
  <div class="ind-band"></div>
  <div class="abs center brand white" style="top:28px;font-size:18px">Datavista</div>
  <div class="abs center" style="top:70px;font-weight:700;font-size:24px;color:var(--white)">Industries We Serve</div>
  <div class="dot fill-navy" style="left:42px;top:134px;width:46px;height:46px;border:2px solid #fff"><svg width="20" height="20" viewBox="0 0 20 20" fill="none" stroke="#fff" stroke-width="1.5"><circle cx="4" cy="4" r="2"/><circle cx="16" cy="4" r="2"/><circle cx="10" cy="10" r="2"/><circle cx="4" cy="16" r="2"/><circle cx="16" cy="16" r="2"/><path d="M5.5 5.5l3 3M14.5 5.5l-3 3M5.5 14.5l3-3M14.5 14.5l-3-3"/></svg></div>
  <div class="dot fill-navy" style="left:150px;top:134px;width:46px;height:46px;border:2px solid #fff"><svg width="20" height="20" viewBox="0 0 20 20" fill="none" stroke="#fff" stroke-width="1.5"><rect x="4" y="6" width="12" height="9" rx="2"/><circle cx="8" cy="10" r="1"/><circle cx="12" cy="10" r="1"/><path d="M10 2v4M2 10h2M16 10h2"/></svg></div>
  <div class="dot fill-navy" style="left:258px;top:134px;width:46px;height:46px;border:2px solid #fff"><svg width="20" height="20" viewBox="0 0 20 20" fill="none" stroke="#fff" stroke-width="1.5"><rect x="5" y="4" width="10" height="14" rx="1"/><path d="M7 2h6M8 9h4v5H8z"/></svg></div>
  <div class="dot fill-navy" style="left:366px;top:134px;width:46px;height:46px;border:2px solid #fff"><svg width="20" height="20" viewBox="0 0 20 20" fill="none" stroke="#fff" stroke-width="1.5"><path d="M3 17l6-6M9 11l8-8-2 7-6 1z M3 14h8"/></svg></div>
  <div class="dot fill-navy" style="left:474px;top:134px;width:46px;height:46px;border:2px solid #fff"><svg width="20" height="20" viewBox="0 0 20 20" fill="none" stroke="#fff" stroke-width="1.5"><path d="M11 2L5 11h5l-1 7 6-9h-5z"/></svg></div>
  <div class="ind" style="left:15px;top:186px"><div class="hd">Chemical<br>Industry</div></div>
  <div class="ind" style="left:123px;top:186px"><div class="hd">Automotive</div></div>
  <div class="ind" style="left:231px;top:186px"><div class="hd">Automotive</div></div>
  <div class="ind" style="left:339px;top:186px"><div class="hd">Mining And<br>Metals</div></div>
  <div class="ind" style="left:447px;top:186px"><div class="hd">Energy</div></div>
  <p class="ind mini" style="left:15px;top:218px">Lorem ipsum dolor sit amet, consectetur adipiscing elit. Vivamus eu dui ex. Curabitur dapibus dignissim dui, in molestie metus feugiat sed. Praesent aliquet lorem ex.</p>
  <p class="ind mini" style="left:123px;top:218px">Lorem ipsum dolor sit amet, consectetur adipiscing elit. Vivamus eu dui ex. Curabitur dapibus dignissim dui, in molestie metus feugiat sed. Praesent aliquet lorem ex.</p>
  <p class="ind mini" style="left:231px;top:218px">Lorem ipsum dolor sit amet, consectetur adipiscing elit. Vivamus eu dui ex. Curabitur dapibus dignissim dui, in molestie metus feugiat sed. Praesent aliquet lorem ex.</p>
  <p class="ind mini" style="left:339px;top:218px">Lorem ipsum dolor sit amet, consectetur adipiscing elit. Vivamus eu dui ex. Curabitur dapibus dignissim dui, in molestie metus feugiat sed. Praesent aliquet lorem ex.</p>
  <p class="ind mini" style="left:447px;top:218px">Lorem ipsum dolor sit amet, consectetur adipiscing elit. Vivamus eu dui ex. Curabitur dapibus dignissim dui, in molestie metus feugiat sed. Praesent aliquet lorem ex.</p>
  <div class="foot-brand">Datavista</div><div class="foot-bar"></div><div class="foot-num">8</div>
</div>

<!-- Row 5 -->
<div class="slide col-l" style="top:2148px">
  <div class="s-title">Slide Title Goes Here</div>
  <div class="dot fill-navy" style="left:75px;top:83px;width:74px;height:74px"><svg width="30" height="30" viewBox="0 0 30 30" fill="none" stroke="#fff" stroke-width="2"><path d="M15 4a8 8 0 0 0-5 14v4h10v-4a8 8 0 0 0-5-14z M11 25h8M12 28h6"/></svg></div>
  <div class="dot fill-sky" style="left:244px;top:83px;width:74px;height:74px"><svg width="32" height="30" viewBox="0 0 32 30" fill="none" stroke="#fff" stroke-width="2"><rect x="6" y="6" width="20" height="14"/><path d="M3 24h26"/></svg></div>
  <div class="dot fill-grey" style="left:413px;top:83px;width:74px;height:74px"><svg width="32" height="24" viewBox="0 0 32 24" fill="#fff"><path d="M8 22a6 6 0 0 1 0-12 9 9 0 0 1 17 2 5 5 0 0 1 0 10z"/></svg></div>
  <div class="abs hd" style="left:37px;width:150px;top:167px;text-align:center">Heading Goes Here</div>
  <div class="abs hd sky" style="left:206px;width:150px;top:167px;text-align:center">Heading Goes Here</div>
  <div class="abs hd grey" style="left:375px;width:150px;top:167px;text-align:center">Heading Goes Here</div>
  <p class="abs tiny" style="left:40px;width:145px;top:187px;text-align:center">Lorem ipsum dolor sit amet, consectetur adipiscing elit. Vivamus eu dui ex. Curabitur dapibus dignissim dui, in molestie metus feugiat sed. Praesent aliquet lorem ex, eu dapibus odio varius at. Duis eget tellus porta, consequat lacus vitae.</p>
  <p class="abs tiny" style="left:209px;width:145px;top:187px;text-align:center">Lorem ipsum dolor sit amet, consectetur adipiscing elit. Vivamus eu dui ex. Curabitur dapibus dignissim dui, in molestie metus feugiat sed. Praesent aliquet lorem ex, eu dapibus odio varius at. Duis eget tellus porta, consequat lacus vitae.</p>
  <p class="abs tiny" style="left:378px;width:145px;top:187px;text-align:center">Lorem ipsum dolor sit amet, consectetur adipiscing elit. Vivamus eu dui ex. Curabitur dapibus dignissim dui, in molestie metus feugiat sed. Praesent aliquet lorem ex, eu dapibus odio varius at. Duis eget tellus porta, consequat lacus vitae.</p>
  <div class="foot-brand">Datavista</div><div class="foot-bar"></div><div class="foot-num">9</div>
</div>
<div class="slide col-r" style="top:2148px">
  <div class="s-title" style="font-size:19px">Uso de analytics en máquinas - Casos actuales</div>
  <div class="case-photo" role="img" aria-label="Industrial cold water machinery" style="left:19px;top:80px"></div>
  <div class="case-photo" role="img" aria-label="Automotive paint plant" style="left:284px;top:80px"></div>
  <div class="case-photo" role="img" aria-label="Cable manufacturing spool" style="left:19px;top:172px"></div>
  <div class="case-photo" role="img" aria-label="Transformer core production line" style="left:284px;top:172px"></div>
  <div class="case" style="left:107px;top:82px"><div class="hd">Ahorro energía en cuarto<br>de máquinas.</div><p class="mini">Generación de agua fría para proceso. Variables de consumo energético. Encendido y apagado de equipos por secuencias para ahorrar energía.</p><p class="hl">12% costo de consumo energético</p></div>
  <div class="case" style="left:372px;top:82px"><div class="hd">Ahorro en fabricación<br>de pintura líquida.</div><p class="mini">Control de receta de pintura automotriz. Instrucciones de llenado y producto se digitalizan y se crea un sistema a prueba de fallas.</p><p class="hl">ahorros de 30% costos de operación</p></div>
  <div class="case" style="left:107px;top:174px"><div class="hd">Mantenimiento predictivo<br>fabricación cables.</div><p class="mini">Digitalización de máquinas de elaboración de cable. Control de disponibilidad y tiempo muerto de paros no programados.</p><p class="hl">Predicción falla al 87%. Ahorros operativos de 15%</p></div>
  <div class="case" style="left:372px;top:174px"><div class="hd">Modelo predictivo hornos<br>para núcleos transformadores.</div><p class="mini">Digitalización de variables que afectan la humedad en núcleos para transformadores. Conectividad y modelo de ahorro.</p><p class="hl">materiales del 1% y 25% en disponibilidad eficiencia</p></div>
  <div class="foot-brand">Datavista</div><div class="foot-bar"></div><div class="foot-num">10</div>
</div>

<!-- Row 6 -->
<div class="slide col-l" style="top:2483px">
  <div class="photo-tunnel" role="img" aria-label="Blue data tunnel with glowing circuit lights" style="bottom:159px"></div>
  <div class="abs center brand white" style="top:30px;font-size:16px">Datavista</div>
  <div class="abs center" style="top:70px;font-weight:700;font-size:24px;color:var(--white)">Expositors</div>
  <div class="dot fill-navy" style="left:75px;top:120px;width:74px;height:74px;border:3px solid #fff"><svg width="30" height="30" viewBox="0 0 30 30" fill="#fff"><circle cx="15" cy="13" r="9"/><path d="M10 20l-3 8 5-2 3 3 2-9zM20 20l3 8-5-2-3 3-2-9z"/></svg></div>
  <div class="dot fill-sky" style="left:244px;top:120px;width:74px;height:74px;border:3px solid #fff"><svg width="30" height="30" viewBox="0 0 30 30" fill="#fff"><path d="M8 4h14v6a7 7 0 0 1-14 0z M13 17h4v5h-4z M9 23h12v4H9z"/></svg></div>
  <div class="dot fill-grey" style="left:413px;top:120px;width:74px;height:74px;border:3px solid #fff"><svg width="30" height="30" viewBox="0 0 30 30" fill="#fff"><rect x="5" y="18" width="5" height="8"/><rect x="12" y="13" width="5" height="13"/><rect x="19" y="9" width="5" height="17"/><path d="M5 12l8-6 5 3 7-5" stroke="#fff" stroke-width="2" fill="none"/></svg></div>
  <div class="abs hd" style="left:37px;width:150px;top:209px;text-align:center;font-size:13px">Your Heading<br>Goes Here</div>
  <div class="abs hd sky" style="left:206px;width:150px;top:209px;text-align:center;font-size:13px">Your Heading<br>Goes Here</div>
  <div class="abs hd grey" style="left:375px;width:150px;top:209px;text-align:center;font-size:13px">Your Heading<br>Goes Here</div>
  <div class="foot-brand">Datavista</div><div class="foot-bar"></div><div class="foot-num">11</div>
</div>
<div class="slide col-r" style="top:2483px">
  <div class="photo-dark" role="img" aria-label="Dark blue technology background with circuit lines"></div>
  <div class="brain" role="img" aria-label="Glowing blue brain over a circuit chip"></div>
  <div class="contact">
    <div class="brand">Datavista</div>
    <h3>Contact Us</h3>
    <p class="addr">AV. LOS ROBLES #215, Col. Centro,<br>64000 Monterrey, N.L.</p>
    <ul>
      <li><svg width="9" height="9" viewBox="0 0 10 10" fill="#fff"><path d="M2 1l2 2-1 1.5a6 6 0 0 0 2.5 2.5L7 6l2 2-1.5 1.5C4 9 1 6 .5 2.5z"/></svg>81 5550 0199</li>
      <li><span style="font-size:9px;width:9px">@</span>informes@datavista-mx.example</li>
      <li><svg width="9" height="9" viewBox="0 0 10 10" fill="none" stroke="#fff"><circle cx="5" cy="5" r="4"/><path d="M1 5h8M5 1c2 2 2 6 0 8M5 1c-2 2-2 6 0 8"/></svg>www.datavista-mx.example</li>
    </ul>
  </div>
  <div class="strip light">Copyright © Datavista</div>
</div>

<!-- Row 7 -->
<div class="slide col-c" style="top:2817px">
  <div class="photo-tunnel" role="img" aria-label="Dark blue circuit board background"></div>
  <div class="contact">
    <div class="brand">Datavista</div>
    <h3>Contact Us</h3>
    <p class="addr">AV. LOS ROBLES #215, Col. Centro,<br>64000 Monterrey, N.L.</p>
    <ul>
      <li><svg width="9" height="9" viewBox="0 0 10 10" fill="#fff"><path d="M2 1l2 2-1 1.5a6 6 0 0 0 2.5 2.5L7 6l2 2-1.5 1.5C4 9 1 6 .5 2.5z"/></svg>81 5550 0199</li>
      <li><span style="font-size:9px;width:9px">@</span>informes@datavista-mx.example</li>
      <li><svg width="9" height="9" viewBox="0 0 10 10" fill="none" stroke="#fff"><circle cx="5" cy="5" r="4"/><path d="M1 5h8M5 1c2 2 2 6 0 8M5 1c-2 2-2 6 0 8"/></svg>www.datavista-mx.example</li>
    </ul>
  </div>
  <div class="strip" style="background:#0b1a30">Copyright © Datavista</div>
</div>

</body>
</html>
```